Simple.... Re-Do this One Page site-MarcelVoss.com

The sites name is MarcelVoss.com it is a biography of me which then links to TimepieceHaven.com

Please utilize the TimepieceHaven.com EXACT logo (and colours) for the link to TimepieceHaven.com Please make MarcelVoss.com Classy... cool and simple... we cater to high end clients. I can also submit a photo of myself to use on the site.

See MarcelVoss.com and use (paste) all the info I have posted there on the page you make.

Target Market(s)

Upscale buyers of fine watches up to $100,000.

Requirements
Must have
• Marcel Voss.com is a simple biography page of me that links to Timepiecehaven.com
• You must use my logo for timepiecehaven.com (you can see it at MarcelVoss.com) this logo will be the link to my other site (timepiecehaven.com)
Should not have
• No flash ...nothing tacky...simple and sleek.

```html
<!DOCTYPE html>
<html lang="en">
<head>
<meta charset="utf-8">
<title>Marcel Voss — Vintage Watch Specialist</title>
<link rel="stylesheet" href="https://fonts.googleapis.com/css2?family=Didact+Gothic&family=Arimo:wght@400&display=swap">
<style>
  :root {
    --page: #ffffff;
    --panel: #333333;
    --rule: #8a8a8a;
    --text: #d8d8d8;
    --muted: #9a9a9a;
    --accent: #e31b1b;
    --frame: #c9c9c9;
    --photo: #2f2f2f;
    --body-font: "Arimo", Arial, Helvetica, sans-serif;
    --display-font: "Didact Gothic", "Century Gothic", sans-serif;
  }
  * { box-sizing: border-box; margin: 0; padding: 0; }
  html, body { width: 1200px; height: 900px; overflow: hidden; background: var(--page); }
  body { position: relative; font-family: var(--body-font); color: var(--text); font-size: 14px; line-height: 17px; }

  .bio-panel { position: absolute; left: 150px; top: 130px; width: 900px; height: 640px; background: var(--panel); }
  .bio-panel > * { position: absolute; }

  .site-name { left: 68px; top: 44px; font-family: var(--display-font); font-size: 40px; line-height: 48px; color: #e6e6e6; letter-spacing: -0.5px; }
  .tagline { left: 332px; top: 57px; font-family: var(--display-font); font-size: 19px; line-height: 24px; color: #e6e6e6; }
  .tagline em { font-style: normal; color: var(--accent); }

  .rule { left: 100px; width: 700px; height: 2px; background: var(--rule); }
  .rule--top { top: 118px; }
  .rule--mid { top: 390px; }
  .rule--bottom { top: 588px; }
  .divider { left: 449px; top: 400px; width: 2px; height: 180px; background: var(--rule); }

  .portrait { left: 100px; top: 138px; width: 132px; height: 132px; border: 10px solid var(--frame); background: var(--photo); }

  .intro { left: 250px; top: 148px; width: 560px; }
  .intro p { margin-bottom: 16px; }
  .intro .drop { color: var(--accent); font-size: 24px; line-height: 17px; }
  .bio-text { left: 100px; top: 291px; width: 700px; }
  .bio-text p { margin-bottom: 16px; }

  .collection { left: 100px; top: 407px; width: 340px; }
  .collection-link { display: block; margin-top: 40px; font-size: 34px; line-height: 40px; color: #d0d0d0; text-decoration: none; letter-spacing: -0.5px; }
  .selling { left: 100px; top: 545px; }

  .contact { left: 465px; top: 407px; width: 340px; font-size: 14px; }
  .contact-row { position: absolute; left: 0; display: flex; width: 340px; }
  .contact-label { width: 95px; color: var(--muted); font-size: 13px; }
  .contact-sep { width: 70px; color: var(--muted); font-size: 13px; }
  .contact-value a { color: var(--text); }
  .row-address { top: 0; }
  .row-email { top: 90px; }
  .row-phone { top: 120px; }
  .memberships { left: 465px; top: 562px; color: var(--muted); font-size: 13px; }
</style>
</head>
<body>
  <main class="bio-panel">
    <h1 class="site-name">Marcel Voss</h1>
    <p class="tagline">Vintage <em>Watch</em> Specialist</p>
    <div class="rule rule--top"></div>

    <div class="portrait" role="img" aria-label="Portrait photo of Marcel Voss"></div>

    <div class="intro">
      <p><span class="drop">M</span>arcel Voss offers offers fine vintage, used and some modern watches for sale.</p>
      <p>He is one of the world's first internet watch dealers - (since 1998 online).</p>
      <p>With over 25 years of high grade vintage watch expertise, Marcel as sold watches to The Royal Family, world dignitaries, the movie industry, noted musicians, actors, writers, artists, fortune 500 CEO's, ultra-elite boutiques and collectors.</p>
    </div>

    <div class="bio-text">
      <p>His timepieces are serviced and ready to wear on your wrist. Marcel has written articles regarding watches appearing in numerous magazines, websites and has supplied historic information, photos and pricing, to a published Vintage Wristwatch "coffee table" book by Halden Press.</p>
      <p>Marcel is one of the world's leading vintage watch experts.</p>
    </div>

    <div class="rule rule--mid"></div>
    <div class="divider"></div>

    <div class="collection">
      <p>To see Marcels online collection visit:</p>
      <a class="collection-link" href="#">TimepieceHaven.com</a>
    </div>
    <p class="selling">Thinking of selling your watch?<br>We buy vintage, QUALITY watches... "Working or Not!"</p>

    <div class="contact">
      <div class="contact-row row-address">
        <span class="contact-label">Contact Details</span><span class="contact-sep">:</span>
        <span class="contact-value">TimepieceHaven.com<br>418 Bellmont Ave.<br>Eastfield, Ontario<br>Canada K7R 4M2</span>
      </div>
      <div class="contact-row row-email">
        <span class="contact-label">Email</span><span class="contact-sep">:</span>
        <span class="contact-value"><a href="#">sales@timepiecehaven.com</a></span>
      </div>
      <div class="contact-row row-phone">
        <span class="contact-label">Telephone</span><span class="contact-sep">:</span>
        <span class="contact-value">613.555.0192</span>
      </div>
    </div>
    <p class="memberships">We are mebers of I.H.G.A. &amp; N.C.W.S.</p>

    <div class="rule rule--bottom"></div>
  </main>
</body>
</html>
```